Help me design my in store poster to promote our Loan product!

We need a design for a 2 X 3 poster inside our stores to promote our installment loan product. We are called Wade's Check Cashing, but offer loans inside our stores. We are open to a new logo for Wade's Loans, and open to any new exciting colors to stand out in the store. We provide short term monthly installment loans, we have monthly payments from 3 - 12 months. Our loans range from $100 - $1,400 with low interest. We ask for ID, consistent source of income, and credit check. We help build credit, and it is fast and easy. We want it to be simple and clean to get people's attention when they are inside our stores. Please help!

UPDATE: The design will be for a 2 X 7 poster now. Less words.

Other font styles liked:
• Rounded corners with the font

Requirements
Must have
• Bold colors, the words: loans, cash, $100 - $1,400, monthly payments, credit building, quick.
Nice to have
• A new logo, the Wade's Check Cashing logo added as reference

UPDATE: If we can add a quick slogan : FAST CASH NOW or HELP IS HERE or YOUR CASH IS HERE or LOANS FOR LIVING or LOANS FOR LIFE

A WADE'S FINANCE LOGO that looks similar to the NOVAJET logo I attached.

```html
<!DOCTYPE html>
<html lang="en">
<head>
<meta charset="utf-8">
<title>Wade's Finance – Cash Loans Poster</title>
<link rel="stylesheet" href="https://fonts.googleapis.com/css2?family=Anton&family=Archivo+Black&family=Archivo:wght@500&display=swap">
<style>
  :root {
    --page-bg: #b6b6b6;
    --royal-blue: #0358a8;
    --navy: #021c66;
    --headline-shadow: #0a1440;
    --charcoal: #2a2a2a;
    --charcoal-deep: #151515;
    --sky: #80c0ff;
    --steel-blue: #7eacd6;
    --brand-navy: #0b4ea6;
    --ink: #232323;
    --red: #c40202;
    --red-deep: #8e0000;
    --brand-red: #e41e26;
    --white: #ffffff;
  }
  html, body {
    margin: 0;
    width: 1200px;
    height: 496px;
    overflow: hidden;
    background: var(--page-bg);
  }
  .poster {
    position: absolute;
    left: 55px;
    top: 90px;
    width: 1079px;
    height: 308px;
    box-shadow: 0 4px 10px rgba(0,0,0,.35);
    display: block;
  }
  .headline { font-family: "Anton", sans-serif; }
  .headline-shadow { fill: var(--headline-shadow); }
  .amount { font-family: "Anton", sans-serif; fill: var(--sky); }
  .range-label { font-family: "Archivo", sans-serif; font-weight: 500; fill: var(--white); }
  .cta-text { font-family: "Archivo Black", sans-serif; fill: var(--white); }
  .feature { font-family: "Archivo Black", sans-serif; }
  .feature--monthly { fill: var(--brand-navy); }
  .feature--credit { fill: var(--steel-blue); }
  .feature--fast { fill: var(--ink); }
  .brand-name { font-family: "Archivo Black", sans-serif; fill: var(--brand-red); }
  .divider { stroke: var(--steel-blue); stroke-width: 1; }
</style>
</head>
<body>
<svg class="poster" viewBox="0 0 1079 308" xmlns="http://www.w3.org/2000/svg" role="img" aria-label="Cash loans from $100 to $1,400. Apply today! Monthly payments, credit building, fast and easy. Wade's Finance.">
  <defs>
    <linearGradient id="chrome" x1="0" y1="0" x2="0" y2="1">
      <stop offset="0" stop-color="#f4f4f4"/>
      <stop offset="0.5" stop-color="#ffffff"/>
      <stop offset="0.52" stop-color="#c9c9c9"/>
      <stop offset="0.75" stop-color="#f2f2f2"/>
      <stop offset="1" stop-color="#d8d8d8"/>
    </linearGradient>
    <linearGradient id="charcoalFade" x1="0" y1="0" x2="0" y2="1">
      <stop offset="0" stop-color="var(--charcoal)"/>
      <stop offset="1" stop-color="var(--charcoal-deep)"/>
    </linearGradient>
    <linearGradient id="ctaRed" x1="0" y1="0" x2="0" y2="1">
      <stop offset="0" stop-color="var(--red)"/>
      <stop offset="1" stop-color="var(--red-deep)"/>
    </linearGradient>
  </defs>

  <!-- panels -->
  <rect class="panel-white" x="0" y="0" width="1079" height="308" fill="var(--white)"/>
  <polygon class="panel-charcoal" points="438,0 806,0 730,308 353,308" fill="url(#charcoalFade)"/>
  <polygon class="panel-blue" points="0,0 438,0 353,308 0,308" fill="var(--royal-blue)"/>
  <polygon class="panel-blue-shadow" points="26,20 350,20 412,96 353,308 75,308 26,278" fill="var(--navy)"/>
  <polygon class="accent-wedge" points="758,196 730,308 820,308" fill="var(--steel-blue)"/>

  <!-- headline -->
  <g class="headline">
    <text class="headline-shadow" x="30" y="152" font-size="100" textLength="322" lengthAdjust="spacingAndGlyphs">CASH</text>
    <text x="27" y="148" font-size="100" textLength="322" lengthAdjust="spacingAndGlyphs" fill="url(#chrome)">CASH</text>
    <text class="headline-shadow" x="31" y="279" font-size="87" textLength="329" lengthAdjust="spacingAndGlyphs">LOANS</text>
    <text x="28" y="275" font-size="87" textLength="329" lengthAdjust="spacingAndGlyphs" fill="url(#chrome)">LOANS</text>
  </g>

  <!-- loan range -->
  <text class="range-label" x="443" y="57" font-size="29" textLength="294" lengthAdjust="spacingAndGlyphs">LOANS RANGE FROM</text>
  <text class="amount" x="434" y="124" font-size="62" textLength="306" lengthAdjust="spacingAndGlyphs">$100 - $1,400</text>

  <!-- call to action -->
  <path class="cta" d="M432,149 H719 Q725,149 725,155 V250 L573,287 L426,250 V155 Q426,149 432,149 Z" fill="url(#ctaRed)" stroke="var(--white)" stroke-width="2"/>
  <text class="cta-text" x="476" y="206" font-size="47" textLength="200" lengthAdjust="spacingAndGlyphs">APPLY</text>
  <text class="cta-text" x="462" y="251" font-size="47" textLength="226" lengthAdjust="spacingAndGlyphs">TODAY!</text>

  <!-- features -->
  <text class="feature feature--monthly" x="844" y="41" font-size="25" textLength="176" lengthAdjust="spacingAndGlyphs">MONTHLY</text>
  <text class="feature feature--monthly" x="833" y="63" font-size="25" textLength="198" lengthAdjust="spacingAndGlyphs">PAYMENTS</text>
  <line class="divider" x1="816" y1="73" x2="1043" y2="73"/>
  <text class="feature feature--credit" x="870" y="101" font-size="25" textLength="125" lengthAdjust="spacingAndGlyphs">CREDIT</text>
  <text class="feature feature--credit" x="852" y="123" font-size="25" textLength="161" lengthAdjust="spacingAndGlyphs">BUILDING</text>
  <line class="divider" x1="816" y1="134" x2="1043" y2="134"/>
  <text class="feature feature--fast" x="818" y="161" font-size="24" textLength="228" lengthAdjust="spacingAndGlyphs">FAST &amp; EASY</text>

  <!-- brand -->
  <text class="brand-name" x="930" y="246" font-size="26" text-anchor="middle">WADE'S FINANCE</text>
</svg>
</body>
</html>
```